Infographic Customizable and DISC Proof

Design of an infographic used to assist candidates to get an overview on the steps they need to take in order to get the candidate in the best possible position to a new step in their career.

Attached is an outline of the text that needs to be converted to an Infographic.

The infographics will be used predominantly as an attachment in the email from the recruiter to the candidate.

Based on the DISC profile of the candidate we require 2 different designs; 1 designed for yellow disc profiles, stylish, beautifull, with the use of our brand color scheme. And one more factual for example for a blue disc profile with far less or no use of colour and a more sleek clean design.

It is important to take into consideration with your design and format you deliver that we want to be able to change some of the content on the infographics after your delivery completely by ourselves for the following use cases:

1. processes differ per client, hence we must be able to add or remove a step and be able to change the title and body of the steps in order to create an infographic for a different client of ours.
2. We would like to be able to change contact details and the profile picture of the recruiter. Example of a profile picture we would want to use is similar to the profile picture of a crestloop profile but then without the background. I attached it as an example for your reference.

It's important to take into consideration that we would need to be able to make such changes by ourselves without the need to become a savvy user of programs such as paint or adobe. The person that would need to be able to make the change is a recruiter, a typical office worker. Please let us know how we would be enabled to do this when you completed the design.

```html
<!DOCTYPE html>
<html lang="nl">
<head>
<meta charset="utf-8">
<title>In 4 stappen optimaal voor het voetlicht</title>
<link rel="stylesheet" href="https://fonts.googleapis.com/css2?family=Bebas+Neue&family=Poppins:wght@500;600;700&display=swap">
<style>
  :root {
    --blue: #1464a8;
    --orange: #f7941d;
    --navy: #0d2a4a;
    --text: #3f4448;
    --rule: #8a8a8a;
    --paper: #ffffff;
  }
  * { margin: 0; padding: 0; box-sizing: border-box; }
  html, body { width: 900px; height: 1200px; overflow: hidden; background: var(--paper); }
  .sheet { position: relative; width: 900px; height: 1200px; font-family: 'Poppins', sans-serif; color: var(--navy); }
  .graphics { position: absolute; inset: 0; }

  .brand-name {
    position: absolute; left: 50px; top: 118px; width: 186px; text-align: center;
    font-weight: 700; font-size: 24px; letter-spacing: 1px; color: var(--blue);
  }
  .headline {
    position: absolute; left: 0; font-family: 'Bebas Neue', sans-serif; line-height: 1; white-space: nowrap;
  }
  .headline--top { left: 268px; top: 52px; font-size: 76px; color: #fff; }
  .headline--bottom { left: 270px; top: 144px; font-size: 76px; color: var(--navy); }

  .step { position: absolute; left: 334px; }
  .step__title { font-size: 23px; font-weight: 600; white-space: nowrap; line-height: 1.2; }
  .step__label { color: var(--blue); font-weight: 700; }
  .step__list { list-style: none; margin-top: 10px; }
  .step__item {
    position: relative; padding-left: 30px; height: 28.5px; line-height: 18px;
    font-size: 13.5px; font-weight: 500; color: var(--text); white-space: nowrap;
  }
  .step__num {
    position: absolute; left: 0; top: 2px; width: 15px; height: 15px; border-radius: 50%;
    border: 1.2px solid var(--orange); color: var(--orange); font-size: 8px; line-height: 13px; text-align: center;
  }
  .step__item:not(:last-child)::after {
    content: ""; position: absolute; left: 7px; top: 18px; height: 10px;
    border-left: 1.5px dotted var(--rule);
  }

  .support { position: absolute; left: 48px; top: 1037px; }
  .support__title { font-size: 21px; font-weight: 600; white-space: nowrap; line-height: 40px; }
  .support__title .accent { color: var(--orange); }
  .support__frame { position: absolute; left: 62px; top: 0; width: 259px; height: 40px; border: 2px solid var(--orange); }
  .support__list { list-style: none; margin-top: 18px; }
  .support__item { position: relative; padding-left: 26px; font-size: 13px; font-weight: 600; line-height: 16px; margin-bottom: 14px; white-space: nowrap; }
  .support__tick { position: absolute; left: 0; top: 1px; }

  .recruiter { position: absolute; left: 480px; top: 1038px; }
  .recruiter__tag {
    position: absolute; left: 7px; top: 0; width: 219px; height: 35px; background: var(--blue);
    border-bottom: 4px solid var(--navy);
    font-family: 'Bebas Neue', sans-serif; font-size: 25px; color: #fff; text-align: center; line-height: 33px;
  }
  .recruiter__name { position: absolute; left: 0; top: 50px; font-size: 27px; font-weight: 700; white-space: nowrap; line-height: 1; left: 1px; }
  .recruiter__name .first { color: var(--orange); }
  .recruiter__role { position: absolute; left: 2px; top: 80px; font-size: 11px; letter-spacing: 8px; color: var(--blue); font-weight: 500; }
  .recruiter__mail { position: absolute; left: 2px; top: 100px; font-size: 14px; font-weight: 500; white-space: nowrap; color: var(--navy); }
  .recruiter__mail svg { vertical-align: -3px; margin-right: 8px; }
</style>
</head>
<body>
<main class="sheet">
  <svg class="graphics" width="900" height="1200" viewBox="0 0 900 1200" aria-hidden="true">
    <defs>
      <linearGradient id="g-blue-left" x1="0" x2="1"><stop offset="0" stop-color="#1464a8"/><stop offset="1" stop-color="#eef1f8"/></linearGradient>
      <linearGradient id="g-orange-left" x1="0" x2="1"><stop offset="0" stop-color="#f7941d"/><stop offset="1" stop-color="#fbefe6"/></linearGradient>
      <linearGradient id="g-blue-right" x1="0" x2="1"><stop offset="0" stop-color="#f2f4f9"/><stop offset="1" stop-color="#1464a8"/></linearGradient>
      <linearGradient id="g-orange-right" x1="0" x2="1"><stop offset="0" stop-color="#fbf1ea"/><stop offset="1" stop-color="#f7941d"/></linearGradient>
      <radialGradient id="g-inner"><stop offset="0.75" stop-color="#fff"/><stop offset="1" stop-color="#e6e6e6"/></radialGradient>
    </defs>

    <!-- header bands -->
    <polygon class="band band--blue" points="185,42 948,42 1005,135 220,135" fill="var(--blue)"/>
    <polygon class="band band--orange" points="220,135 1005,135 948,226 185,226" fill="var(--orange)"/>
    <circle cx="143" cy="133" r="100" fill="#fff"/>
    <circle cx="143" cy="133" r="90" fill="#fff" stroke="var(--orange)" stroke-width="7"/>
    <rect x="126" y="88" width="34" height="24" fill="var(--blue)"/>

    <!-- timeline -->
    <line x1="73" y1="298" x2="73" y2="985" stroke="var(--rule)" stroke-width="1.5" stroke-dasharray="6 4"/>
    <polygon points="73,272 63,289 83,289" fill="var(--navy)"/>
    <polygon points="73,986 63,969 83,969" fill="var(--navy)"/>
    <line x1="73" y1="990" x2="850" y2="990" stroke="var(--rule)" stroke-width="1.5" stroke-dasharray="8 5"/>

    <g class="stage">
      <line x1="87" y1="338" x2="154" y2="338" stroke="var(--rule)" stroke-width="1.8"/>
      <path d="M154,338 C185,338 200,283 242,278 A60,60 0 1 1 242,398 C200,393 185,338 154,338 Z" fill="url(#g-blue-left)"/>
      <circle cx="242" cy="338" r="44" fill="url(#g-inner)"/>
      <circle cx="242" cy="338" r="20" fill="#fde6c9" role="img" aria-label="Pictogram: document met downloadpijl"/>
      <circle cx="73" cy="338" r="15" fill="#fff" stroke="var(--orange)" stroke-width="3"/>
      <circle cx="73" cy="338" r="11" fill="none" stroke="var(--blue)" stroke-width="2.5"/>
    </g>
    <g class="stage">
      <line x1="87" y1="569" x2="154" y2="569" stroke="var(--rule)" stroke-width="1.8"/>
      <path d="M154,569 C185,569 200,514 242,509 A60,60 0 1 1 242,629 C200,624 185,569 154,569 Z" fill="url(#g-orange-left)"/>
      <circle cx="242" cy="569" r="44" fill="url(#g-inner)"/>
      <circle cx="242" cy="569" r="20" fill="#fde6c9" role="img" aria-label="Pictogram: bliksem met uitroeptekens"/>
      <circle cx="73" cy="569" r="15" fill="#fff" stroke="var(--orange)" stroke-width="3"/>
      <circle cx="73" cy="569" r="11" fill="none" stroke="var(--blue)" stroke-width="2.5"/>
    </g>
    <g class="stage">
      <line x1="87" y1="754" x2="154" y2="754" stroke="var(--rule)" stroke-width="1.8"/>
      <path d="M154,754 C185,754 200,699 242,694 A60,60 0 1 1 242,814 C200,809 185,754 154,754 Z" fill="url(#g-blue-right)"/>
      <circle cx="242" cy="754" r="44" fill="url(#g-inner)"/>
      <circle cx="242" cy="754" r="20" fill="#fde6c9" role="img" aria-label="Pictogram: gebalde vuist met pijlen omhoog"/>
      <circle cx="73" cy="754" r="15" fill="#fff" stroke="var(--orange)" stroke-width="3"/>
      <circle cx="73" cy="754" r="11" fill="none" stroke="var(--blue)" stroke-width="2.5"/>
    </g>
    <g class="stage">
      <line x1="87" y1="916" x2="154" y2="916" stroke="var(--rule)" stroke-width="1.8"/>
      <path d="M154,916 C185,916 200,861 242,856 A60,60 0 1 1 242,976 C200,971 185,916 154,916 Z" fill="url(#g-orange-right)"/>
      <circle cx="242" cy="916" r="44" fill="url(#g-inner)"/>
      <circle cx="242" cy="916" r="20" fill="#fde6c9" role="img" aria-label="Pictogram: pijlen in alle richtingen"/>
      <circle cx="73" cy="916" r="15" fill="#fff" stroke="var(--orange)" stroke-width="3"/>
      <circle cx="73" cy="916" r="11" fill="none" stroke="var(--blue)" stroke-width="2.5"/>
    </g>

    <!-- down arrows between stages -->
    <g fill="none" stroke="var(--navy)" stroke-width="1.2">
      <path d="M237,425 V452 H232 L239,462 L246,452 H241 V425 Z"/>
      <path d="M237,650 V677 H232 L239,687 L246,677 H241 V650 Z"/>
      <path d="M237,820 V847 H232 L239,857 L246,847 H241 V820 Z"/>
    </g>

    <!-- recruiter photo -->
    <circle cx="792" cy="1096" r="63" fill="var(--orange)"/>
    <circle cx="792" cy="1096" r="57" fill="url(#g-blue-left)" role="img" aria-label="Profielfoto van de recruiter"/>
  </svg>

  <div class="brand-name">VERINTA</div>
  <h1 class="headline headline--top">IN 4 STAPPEN OPTIMAAL</h1>
  <p class="headline headline--bottom">VOOR HET VOETLICHT</p>

  <section class="step" style="top:274px">
    <h2 class="step__title"><span class="step__label">STEP 1</span> CV voorbereiden</h2>
    <ol class="step__list">
      <li class="step__item"><span class="step__num">1</span>Gebruik het bijgevoegde CV-template</li>
      <li class="step__item"><span class="step__num">2</span>Maximaal 7 pagina's A4</li>
      <li class="step__item"><span class="step__num">3</span>Schrijf in het Nederlands</li>
      <li class="step__item"><span class="step__num">4</span>Volg de specifieke datumnotatie [dd-mm-jjjj]</li>
      <li class="step__item"><span class="step__num">5</span>Vermeld uren per week bij elke functie in het werkverleden</li>
      <li class="step__item"><span class="step__num">6</span>Voeg blokken toe waar nodig</li>
    </ol>
  </section>

  <section class="step" style="top:509px">
    <h2 class="step__title"><span class="step__label">STEP 2</span> Eisen en wensen beargumenteren</h2>
    <ol class="step__list">
      <li class="step__item"><span class="step__num">1</span>Beargumenteer eisen beknopt en herleidbaar</li>
      <li class="step__item"><span class="step__num">2</span>Beargumenteer wensen uitgebreid en kwalitatief</li>
      <li class="step__item"><span class="step__num">3</span>Geef situatieschetsen en voorbeelden van ervaring</li>
      <li class="step__item"><span class="step__num">4</span>Vermeld het aantal maanden ervaring per gevraagd element</li>
    </ol>
  </section>

  <section class="step" style="top:701px">
    <h2 class="step__title"><span class="step__label">STEP 3</span> Motivatie en introductie</h2>
    <ol class="step__list">
      <li class="step__item"><span class="step__num">1</span>Schrijf een korte, persoonlijke introductie</li>
      <li class="step__item"><span class="step__num">2</span>Benadruk jouw kracht en motivatie voor de rol en de organisatie</li>
    </ol>
  </section>

  <section class="step" style="top:859px">
    <h2 class="step__title"><span class="step__label">STEP 4</span> Controleer en verstuur</h2>
    <ol class="step__list">
      <li class="step__item"><span class="step__num">1</span>Schrijf een korte, persoonlijke introductie</li>
      <li class="step__item"><span class="step__num">2</span>Benadruk jouw kracht en motivatie voor de rol en de organisatie</li>
    </ol>
  </section>

  <section class="support">
    <div class="support__frame"></div>
    <h2 class="support__title"><span class="accent">EXTRA</span> ONDERSTEUNING</h2>
    <ul class="support__list">
      <li class="support__item">
        <svg class="support__tick" width="13" height="13" viewBox="0 0 13 13"><circle cx="6.5" cy="6.5" r="5.8" fill="none" stroke="#888" stroke-width="1"/><path d="M4 6.7 L5.9 8.5 L9.2 4.8" fill="none" stroke="#888" stroke-width="1.2"/></svg>
        Neem contact op met je toegewezen<br>contactpersoon voor vragen
      </li>
      <li class="support__item">
        <svg class="support__tick" width="13" height="13" viewBox="0 0 13 13"><circle cx="6.5" cy="6.5" r="5.8" fill="none" stroke="#888" stroke-width="1"/><path d="M4 6.7 L5.9 8.5 L9.2 4.8" fill="none" stroke="#888" stroke-width="1.2"/></svg>
        Raadpleeg bijgevoegde voorbeeld beargumentatie
      </li>
    </ul>
  </section>

  <section class="recruiter">
    <div class="recruiter__tag">AANDACHT VOOR IMPACT</div>
    <p class="recruiter__name"><span class="first">RUBEN</span> KOK</p>
    <p class="recruiter__role">RECRUITER</p>
    <p class="recruiter__mail">
      <svg width="16" height="12" viewBox="0 0 16 12"><rect x="0.6" y="0.6" width="14.8" height="10.8" fill="none" stroke="#666" stroke-width="1"/><path d="M0.6 0.6 L8 6.5 L15.4 0.6 M0.6 11.4 L6 5.3 M15.4 11.4 L10 5.3" fill="none" stroke="#666" stroke-width="1"/></svg>info@rubenkok.com
    </p>
  </section>
</main>
</body>
</html>
```